Business Card Design

We Need a business card design for my company based in Tv Radio and music Productions and hunt Talent.

Industry/Entity Type

Business

Contact Information for Business Card

BrentaVue Production's, Teodor Vignoles,Cell Phone 318 4957310
Musician, Productor, Hunt Talent. Miami Fla. www.brentavue.net Mail. teodorvignoles@mailvana.com

```html
<!DOCTYPE html>
<html lang="en">
<head>
<meta charset="utf-8">
<title>BrentaVue Production's – Business Card</title>
<link rel="stylesheet" href="https://fonts.googleapis.com/css2?family=Open+Sans:wght@400;600;700;800&display=swap">
<style>
  :root {
    --bg: #ffffff;
    --yellow-light: #fde27a;
    --yellow: #fcd21c;
    --yellow-deep: #f5c400;
    --gold-light: #f3cf52;
    --gold: #d9ab1e;
    --gold-deep: #9b7a24;
    --orange: #f15a24;
    --ink: #1e1e1e;
    --purple: #6a3c97;
    --white: #ffffff;
  }
  * { margin: 0; padding: 0; box-sizing: border-box; }
  html, body { width: 1200px; height: 900px; overflow: hidden; background: var(--bg); }
  body { font-family: "Open Sans", Arial, sans-serif; position: relative; }

  .card {
    position: absolute;
    top: 290px;
    width: 530px;
    height: 310px;
    border-radius: 22px;
    overflow: hidden;
    box-shadow: 0 10px 28px rgba(0,0,0,0.12);
  }
  .card--front { left: 50px; }
  .card--back { left: 620px; }

  .card__shape { position: absolute; inset: 0; width: 100%; height: 100%; }

  /* front */
  .brand {
    position: absolute;
    left: 18px;
    top: 132px;
    display: flex;
    align-items: center;
    gap: 6px;
  }
  .brand__dot {
    width: 16px; height: 16px; border-radius: 50%;
    background: var(--yellow-deep);
  }
  .brand__name {
    font-weight: 800;
    font-size: 24px;
    color: var(--orange);
    letter-spacing: -0.3px;
  }
  .brand__url {
    position: absolute;
    left: 44px; top: 166px;
    font-size: 10px; font-weight: 700;
    color: var(--orange);
  }

  .holder {
    position: absolute;
    left: 270px; top: 38px;
    font-size: 21px; font-weight: 600;
    color: var(--orange);
    letter-spacing: 0.5px;
    text-transform: uppercase;
  }
  .contacts {
    position: absolute;
    left: 258px; top: 120px;
    list-style: none;
  }
  .contacts__item {
    display: flex; align-items: center; gap: 5px;
    font-size: 14.5px; font-weight: 600;
    color: var(--ink);
    line-height: 21px;
  }
  .contacts__icon { width: 15px; height: 15px; flex: none; }
  .contacts__square {
    width: 14px; height: 14px; flex: none;
    background: var(--orange); border-radius: 2px;
  }
  .roles {
    position: absolute;
    left: 204px; top: 276px;
    font-size: 14px; font-weight: 700;
    color: var(--purple);
    white-space: nowrap;
  }
  .roles span { margin: 0 8px; }

  /* back */
  .back__decor { position: absolute; inset: 0; }
  .back__brand {
    position: absolute;
    left: 0; right: 0; top: 118px;
    display: flex; justify-content: center; align-items: center; gap: 10px;
  }
  .back__dot {
    width: 26px; height: 26px; border-radius: 50%;
    background: var(--orange);
  }
  .back__name {
    font-weight: 800; font-size: 48px;
    color: var(--white);
    letter-spacing: -0.5px;
  }
  .back__url {
    position: absolute;
    left: 0; right: 0; top: 186px;
    text-align: center;
    font-size: 15px; font-weight: 700;
    color: var(--orange);
  }
</style>
</head>
<body>

<section class="card card--front" aria-label="Business card, front">
  <svg class="card__shape" viewBox="0 0 530 310" preserveAspectRatio="none" aria-hidden="true">
    <defs>
      <linearGradient id="frontYellow" x1="0" y1="0" x2="1" y2="1">
        <stop offset="0" stop-color="var(--yellow-light)"/>
        <stop offset="0.5" stop-color="var(--yellow)"/>
        <stop offset="1" stop-color="var(--yellow-deep)"/>
      </linearGradient>
    </defs>
    <rect width="530" height="310" fill="url(#frontYellow)"/>
    <path d="M0 0 H218 Q196 150 150 310 H0 Z" fill="var(--orange)"/>
    <path d="M0 0 H188 Q176 150 140 310 H0 Z" fill="var(--white)"/>
    <path d="M218 0 Q196 150 150 310" fill="none" stroke="var(--ink)" stroke-width="1.5"/>
  </svg>

  <div class="brand">
    <span class="brand__name">BrentaVue</span>
    <span class="brand__dot"></span>
  </div>
  <p class="brand__url">www.brentavue.net</p>

  <h1 class="holder">Teodor Vignoles</h1>

  <ul class="contacts">
    <li class="contacts__item">
      <svg class="contacts__icon" viewBox="0 0 24 24" aria-hidden="true"><path fill="var(--orange)" d="M6.6 10.8a15.1 15.1 0 0 0 6.6 6.6l2.2-2.2a1 1 0 0 1 1-.25 11.4 11.4 0 0 0 3.6.57 1 1 0 0 1 1 1V20a1 1 0 0 1-1 1A17 17 0 0 1 3 4a1 1 0 0 1 1-1h3.5a1 1 0 0 1 1 1c0 1.25.2 2.45.57 3.57a1 1 0 0 1-.25 1z"/></svg>
      USA, Miami, Fla 318-495-7310
    </li>
    <li class="contacts__item">
      <svg class="contacts__icon" viewBox="0 0 24 24" aria-hidden="true"><path fill="var(--orange)" d="M6.6 10.8a15.1 15.1 0 0 0 6.6 6.6l2.2-2.2a1 1 0 0 1 1-.25 11.4 11.4 0 0 0 3.6.57 1 1 0 0 1 1 1V20a1 1 0 0 1-1 1A17 17 0 0 1 3 4a1 1 0 0 1 1-1h3.5a1 1 0 0 1 1 1c0 1.25.2 2.45.57 3.57a1 1 0 0 1-.25 1z"/></svg>
      Venezuela +58-414 5203864
    </li>
    <li class="contacts__item">
      <svg class="contacts__icon" viewBox="0 0 24 24" aria-hidden="true"><g fill="none" stroke="var(--orange)" stroke-width="2"><circle cx="12" cy="12" r="9.5"/><ellipse cx="12" cy="12" rx="4.5" ry="9.5"/><path d="M2.5 12h19M4.5 7h15M4.5 17h15"/></g></svg>
      www.brentavue.net
    </li>
    <li class="contacts__item">
      <svg class="contacts__icon" viewBox="0 0 24 24" aria-hidden="true"><rect x="1.5" y="4.5" width="21" height="15" rx="1.5" fill="var(--orange)"/><path d="M2.5 6l9.5 7 9.5-7" fill="none" stroke="var(--white)" stroke-width="1.8"/></svg>
      teodorvignoles@mailvana.com
    </li>
    <li class="contacts__item">
      <span class="contacts__square"></span>
      @brentavue
    </li>
  </ul>

  <p class="roles">Musician<span>|</span>Tv Producer<span>|</span>Hunt Talent</p>
</section>

<section class="card card--back" aria-label="Business card, back">
  <svg class="card__shape" viewBox="0 0 530 310" preserveAspectRatio="none" aria-hidden="true">
    <defs>
      <linearGradient id="backGold" x1="0" y1="0" x2="1" y2="1">
        <stop offset="0" stop-color="var(--gold-light)"/>
        <stop offset="0.55" stop-color="var(--gold)"/>
        <stop offset="1" stop-color="var(--gold-deep)"/>
      </linearGradient>
    </defs>
    <rect width="530" height="310" fill="url(#backGold)"/>
  </svg>
  <div class="back__decor" role="img" aria-label="Soft gold backdrop with fine flowing light lines and sparkles"
       style="background: radial-gradient(ellipse at 25% 20%, rgba(255,255,255,0.35), transparent 55%), radial-gradient(ellipse at 60% 85%, rgba(255,240,180,0.25), transparent 60%);"></div>

  <div class="back__brand">
    <span class="back__name">BrentaVue</span>
    <span class="back__dot"></span>
  </div>
  <p class="back__url">www.brentavue.net</p>
</section>

</body>
</html>
```